Pellworth and Tasker Ranch Insurance

Would like you all to design a logo for our Business cards and possible letterhead.
This business provides Ranch insurance for folks in Texas, New Mexico, and Oklahoma

Ggood stuff everybody, be sure to include email and Mobil for both of us on all designs

Thanks

Hello All

Wanted to let you all know i am going to extend deadline a few days, and add some more $$ to the budget

Reason: Give everybody a bit ,more time, and I added more money

Appreciate all of yalls hard work, will review and provide feed back hopefully today, been a little whacky with the holidays and all

Industry/Entity Type

Business

```html
<!DOCTYPE html>
<html lang="en">
<head>
<meta charset="utf-8">
<title>Pellworth and Tasker – Business Card</title>
<link rel="stylesheet" href="https://fonts.googleapis.com/css2?family=Questrial&family=Saira:wght@500&display=swap">
<style>
  :root {
    --stage: #a3a3a3;
    --paper: #ffffff;
    --ink: #111111;
    --orange: #ea7a22;
    --orange-light: #f7a23e;
    --dark-top: #2f3133;
    --dark-bottom: #1f2021;
    --light-text: #ffffff;
    --divider: #c9c9c9;
  }
  * { box-sizing: border-box; margin: 0; padding: 0; }
  html, body {
    width: 1200px; height: 900px; overflow: hidden;
    background: var(--stage);
  }
  .card {
    position: absolute; left: 100px; top: 142px;
    width: 1000px; height: 616px;
    background: var(--paper);
    font-family: "Questrial", sans-serif;
  }
  .brand {
    position: absolute; left: 71px; top: 105px;
    display: flex; align-items: center; gap: 32px;
  }
  .brand-square {
    width: 160px; height: 160px; background: var(--orange);
  }
  .brand-name {
    font-family: "Saira", sans-serif; font-weight: 500;
    font-size: 52px; color: var(--ink); letter-spacing: 0.5px;
  }
  .slogan-band {
    position: absolute; left: 0; top: 289px; width: 100%; height: 27px;
    background: linear-gradient(90deg, var(--orange), var(--orange-light) 50%, var(--orange));
    display: flex; align-items: center; justify-content: center;
    font-family: "Saira", sans-serif; font-weight: 500;
    font-size: 15px; letter-spacing: 20px; color: var(--ink);
    padding-left: 20px;
  }
  .info-panel {
    position: absolute; left: 0; top: 316px; width: 100%; height: 300px;
    background: linear-gradient(180deg, var(--dark-top), var(--dark-bottom));
    color: var(--light-text);
  }
  .office {
    position: absolute; right: 522px; top: 60px;
    text-align: right; font-size: 27px; line-height: 37px;
  }
  .office-line { display: flex; justify-content: flex-end; align-items: center; gap: 10px; }
  .office-line .icon-slot { width: 32px; height: 32px; display: inline-flex; }
  .divider {
    position: absolute; left: 529px; top: 23px;
    width: 2px; height: 205px; background: var(--divider);
  }
  .partners { position: absolute; left: 572px; top: 28px; }
  .partner + .partner { margin-top: 26px; }
  .partner-name {
    color: var(--orange); font-size: 27px; line-height: 34px; padding-left: 28px;
  }
  .partner-line {
    display: flex; align-items: center; gap: 4px;
    font-size: 24px; line-height: 32px;
  }
  .partner-line svg { width: 24px; height: 24px; flex: none; }
  svg { fill: var(--orange); }
</style>
</head>
<body>
  <div class="card">
    <div class="brand">
      <div class="brand-square"></div>
      <div class="brand-name">Pellworth and Tasker</div>
    </div>

    <div class="slogan-band">COMPANY SLOGON GOSE HERE</div>

    <div class="info-panel">
      <div class="office">
        <div class="office-line">325.555.0148
          <span class="icon-slot"><svg viewBox="0 0 24 24" width="32" height="32"><path d="M6.6 10.8c1.4 2.8 3.8 5.1 6.6 6.6l2.2-2.2c.3-.3.7-.4 1-.2 1.1.4 2.3.6 3.6.6.6 0 1 .4 1 1V20c0 .6-.4 1-1 1C10.6 21 3 13.4 3 4c0-.6.4-1 1-1h3.5c.6 0 1 .4 1 1 0 1.3.2 2.5.6 3.6.1.3 0 .7-.2 1z"/></svg></span>
        </div>
        <div class="office-line">408 W Pecan St.
          <span class="icon-slot"><svg viewBox="0 0 24 24" width="32" height="32"><path d="M12 3 2 12h3v9h5v-6h4v6h5v-9h3z"/></svg></span>
        </div>
        <div class="office-line">Brushy Creek, TX 76998
          <span class="icon-slot"></span>
        </div>
        <div class="office-line">www.pellworthandtasker.com
          <span class="icon-slot"><svg viewBox="0 0 24 24" width="32" height="32" fill="none" stroke="#ea7a22" stroke-width="1.6"><circle cx="12" cy="12" r="9"/><ellipse cx="12" cy="12" rx="4" ry="9"/><path d="M3 12h18M5 7h14M5 17h14"/></svg></span>
        </div>
      </div>

      <div class="divider"></div>

      <div class="partners">
        <div class="partner">
          <div class="partner-name">Ned Tasker</div>
          <div class="partner-line">
            <svg viewBox="0 0 24 24"><path d="M2 6h20v13H2z" opacity=".9"/><path d="M2 6l10 7 10-7" fill="none" stroke="#2a2b2c" stroke-width="1.6"/></svg>
            ned@pellworthandtasker.com
          </div>
          <div class="partner-line">
            <svg viewBox="0 0 24 24"><rect x="6" y="2" width="12" height="20" rx="2"/><rect x="8" y="4" width="8" height="7" fill="#2a2b2c"/></svg>
            cell #325-555-0172
          </div>
        </div>
        <div class="partner">
          <div class="partner-name">Hal Pellworth</div>
          <div class="partner-line">
            <svg viewBox="0 0 24 24"><path d="M2 6h20v13H2z" opacity=".9"/><path d="M2 6l10 7 10-7" fill="none" stroke="#2a2b2c" stroke-width="1.6"/></svg>
            pellworthh@ranvo.com
          </div>
          <div class="partner-line">
            <svg viewBox="0 0 24 24"><rect x="6" y="2" width="12" height="20" rx="2"/><rect x="8" y="4" width="8" height="7" fill="#2a2b2c"/></svg>
            cell # 512-555-0193
          </div>
        </div>
      </div>
    </div>
  </div>
</body>
</html>
```